Willow Glow & Laser - Business Banner with Brand Elements

Design:
• We would like to get a creative design for a wide banner that will go outside our medical spa clinic location. We need a designer to make a simple yet colorful and high-quality design layout. We want this banner to be eye-catching and to communicate the services we offer at our business: Laser Hair Removal | Velonix | Lip Filler.

Requirements:
• We would like the banner to include our companies information which is the following:

Logo
“Refresh Your Skin”
Laser Hair Removal | Velonix | Lip Filler
(555) 287-1936
www.WillowGlowLaser.com

Colors:
• Our business colors are orange, a hint of black and white, but mostly peach/orange tones. (Orange: #f78f20 , White: #ffffff)

Fonts:
• Josefins Sans Bold & Lato

Content and images can be located here:
https://files.cloudvaultshare.com/folders/7tQmZ2xVbR9kLpN4sW8yH3cD6fJ1gA0eU?usp=sharing

The following will give you an idea of our brand presentation:
• Our website is: www.WillowGlowLaser.com
• Our Instagram; @willowglowlaser
• Our Facebook: www.socialpagehub.com/willowglowlaser

Target Market(s)
• Women 25 - 45

Industry/Entity Type
• Beauty

```html
<!DOCTYPE html>
<html lang="en">
<head>
<meta charset="utf-8">
<title>Willow Glow &amp; Laser – Banner Concepts</title>
<link href="https://fonts.googleapis.com/css2?family=Josefin+Sans:wght@400;600;700&family=Lato:wght@400;700&display=swap" rel="stylesheet">
<style>
:root{
  --orange:#f78f20;
  --orange-deep:#ef7a0c;
  --orange-soft:#fba543;
  --peach:#fdc58a;
  --white:#ffffff;
  --ink:#111111;
  --paper:#f7f7f7;
  --sea:#5cc4d8;
  --sand:#efe3d2;
}
*{margin:0;padding:0;box-sizing:border-box}
html,body{width:1200px;height:856px;overflow:hidden;background:var(--white)}
body{position:relative;font-family:"Josefin Sans",sans-serif}
.banner{position:absolute;width:561px;height:341px;overflow:hidden;box-shadow:0 1px 4px rgba(0,0,0,.12)}
.banner svg{position:absolute;left:0;top:0}
.abs{position:absolute}
.brand{position:absolute;display:flex;align-items:center;gap:8px;font-weight:700;line-height:1}
.brand-dot{border-radius:50%;flex:none}
.headline{position:absolute;font-weight:700;line-height:1;white-space:nowrap}
.services,.contact{position:absolute;font-weight:400;white-space:nowrap;letter-spacing:.3px}
.social{position:absolute;display:flex;gap:3px}
.social span{display:block;width:26px;height:26px;border-radius:50%}

/* banner 1 */
.b1{left:31px;top:69px;background:var(--paper)}
.b1 .brand{left:22px;top:52px;font-size:30px;color:var(--ink)}
.b1 .brand-dot{width:36px;height:36px;background:var(--orange)}
.b1 .headline{left:20px;top:232px;font-size:34px;color:var(--white)}
.b1 .services{left:21px;top:272px;font-size:14px;color:var(--white)}
.b1 .contact{left:21px;top:303px;font-size:13px;color:var(--white)}
.b1 .social{right:23px;top:297px}
.b1 .social span{background:var(--white)}

/* banner 2 */
.b2{left:610px;top:66px;background:var(--orange-soft)}
.b2 .brand{left:0;width:360px;justify-content:center;top:70px;font-size:24px;color:var(--white)}
.b2 .brand-dot{width:30px;height:30px;background:var(--white)}
.b2 .headline{left:0;width:360px;text-align:center;top:122px;font-size:31px;color:var(--white)}
.b2 .services{left:0;width:360px;text-align:center;top:164px;font-size:15px;color:var(--white)}
.b2 .phone{position:absolute;left:0;width:360px;text-align:center;top:198px;font-size:23px;color:var(--white)}
.b2 .contact{left:0;width:360px;text-align:center;top:228px;font-size:9px;color:var(--white)}
.b2 .social{left:153px;top:248px}
.b2 .social span{background:var(--white)}

/* banner 3 */
.b3{left:29px;top:454px;background:var(--orange)}
.b3 .brand{left:18px;top:40px;font-size:28px;color:var(--white)}
.b3 .brand-dot{width:36px;height:36px;background:var(--white)}
.b3 .headline{left:17px;top:133px;font-size:30px;color:var(--white)}
.b3 .services{left:18px;top:169px;font-size:13px;color:var(--white)}
.b3 .contact{left:18px;top:200px;font-size:13px;line-height:21px;color:var(--white)}
.b3 .social{left:19px;top:293px}
.b3 .social span{background:var(--white)}

/* banner 4 */
.b4{left:610px;top:454px;background:var(--paper)}
.b4 .brand{left:12px;top:30px;font-size:22px;color:var(--ink);width:150px;flex-wrap:nowrap}
.b4 .brand-dot{width:30px;height:30px;background:var(--orange)}
.b4 .headline{left:17px;top:133px;font-size:34px;line-height:33px;color:var(--ink)}
.b4 .services{left:17px;top:212px;font-size:18px;line-height:24px;color:var(--orange)}
.b4 .contact{left:17px;top:266px;font-size:10px;color:#333}
.b4 .social{left:18px;top:289px}
.b4 .social span{background:var(--orange)}
</style>
</head>
<body>

<!-- Concept 1 -->
<section class="banner b1">
  <svg width="561" height="341" viewBox="0 0 561 341">
    <defs>
      <linearGradient id="beach1" x1="0" y1="0" x2="1" y2="1">
        <stop offset="0" stop-color="#d9f0f4"/><stop offset=".5" stop-color="var(--sea)"/><stop offset="1" stop-color="#c98e63"/>
      </linearGradient>
    </defs>
    <rect x="270" y="0" width="291" height="270" fill="url(#beach1)" role="img" aria-label="Photo of a smiling woman in a straw hat on a sunny beach"/>
    <path d="M0,180 C70,150 160,140 270,185 C370,230 470,300 561,190 L561,341 L0,341 Z" fill="var(--orange)"/>
    <path d="M0,215 C90,180 200,200 300,260 C400,320 480,300 561,260 L561,341 L0,341 Z" fill="var(--orange-deep)"/>
  </svg>
  <div class="brand"><span class="brand-dot"></span>Willow Glow &amp; Laser</div>
  <h1 class="headline">Refresh Your Skin</h1>
  <p class="services">Laser Hair Removal | Velonix | Lip Filler</p>
  <p class="contact">(555) 287-1936 / www.WillowGlowLaser.com</p>
  <div class="social"><span></span><span></span></div>
</section>

<!-- Concept 2 -->
<section class="banner b2">
  <svg width="561" height="341" viewBox="0 0 561 341">
    <defs>
      <linearGradient id="portrait2" x1="0" y1="0" x2="0" y2="1">
        <stop offset="0" stop-color="#f1c7a4"/><stop offset=".6" stop-color="#eab690"/><stop offset="1" stop-color="#f6e6d6"/>
      </linearGradient>
    </defs>
    <path d="M0,130 L160,0 L560,0 L560,341 L150,341 L0,200 Z" fill="var(--orange)" opacity=".5"/>
    <path d="M420,110 L490,60 L561,120 L490,180 Z" fill="var(--orange-soft)"/>
    <g stroke="var(--peach)" stroke-width="1.6" fill="none">
      <line x1="10" y1="83" x2="82" y2="16"/>
      <line x1="14" y1="262" x2="85" y2="330"/>
      <path d="M455,125 L532,75 L561,100"/>
      <path d="M240,250 L300,220 L330,270"/>
    </g>
    <rect x="300" y="0" width="261" height="341" fill="url(#portrait2)" role="img" aria-label="Photo of a smiling woman in a cream camisole touching her shoulder"/>
  </svg>
  <div class="brand"><span class="brand-dot"></span>Willow Glow &amp; Laser</div>
  <h1 class="headline">Refresh Your Skin</h1>
  <p class="services">Laser Hair Removal | Velonix | Lip Filler</p>
  <p class="phone">(555) 287-1936</p>
  <p class="contact">www.WillowGlowLaser.com</p>
  <div class="social"><span></span><span></span></div>
</section>

<!-- Concept 3 -->
<section class="banner b3">
  <svg width="561" height="342" viewBox="0 0 561 342">
    <defs>
      <linearGradient id="beach3" x1="0" y1="0" x2="0" y2="1">
        <stop offset="0" stop-color="#bfe6ef"/><stop offset=".45" stop-color="#8fcfd9"/><stop offset=".7" stop-color="#e7d2bb"/><stop offset="1" stop-color="#f0e6da"/>
      </linearGradient>
    </defs>
    <path d="M0,290 C120,260 250,300 320,342 L0,342 Z" fill="var(--orange-deep)" opacity=".6"/>
    <circle cx="512" cy="82" r="250" fill="#ff9f0a"/>
    <circle cx="512" cy="74" r="245" fill="url(#beach3)" role="img" aria-label="Photo of a laughing woman with windblown hair on the beach"/>
    <g stroke="var(--white)" stroke-width="1.4">
      <line x1="246" y1="278" x2="308" y2="222"/>
      <line x1="252" y1="280" x2="312" y2="226"/>
    </g>
  </svg>
  <div class="brand"><span class="brand-dot"></span>Willow Glow &amp; Laser</div>
  <h1 class="headline">Refresh Your Skin</h1>
  <p class="services">Laser Hair Removal | Velonix | Lip Filler</p>
  <p class="contact">(555) 287-1936<br>www.WillowGlowLaser.com</p>
  <div class="social"><span></span><span></span></div>
</section>

<!-- Concept 4 -->
<section class="banner b4">
  <svg width="561" height="342" viewBox="0 0 561 342">
    <path d="M165,0 L180,0 C195,190 380,295 561,290 L561,342 L410,342 C260,320 165,200 165,0 Z" fill="var(--orange)"/>
  </svg>
  <svg width="561" height="342" viewBox="0 0 561 342" role="img" aria-label="Photo of a smiling woman lying on the sand at the water's edge">
    <defs>
      <linearGradient id="beach4" x1="0" y1="0" x2="0" y2="1">
        <stop offset="0" stop-color="#e5eef4"/><stop offset=".15" stop-color="#36b6cc"/><stop offset=".55" stop-color="#8fd3d6"/><stop offset="1" stop-color="#efe0cc"/>
      </linearGradient>
    </defs>
    <path d="M182,0 L561,0 L561,282 C390,285 200,185 182,0 Z" fill="url(#beach4)"/>
  </svg>
  <div class="brand"><span class="brand-dot"></span>Willow Glow &amp; Laser</div>
  <h1 class="headline">Refresh<br>Your Skin</h1>
  <p class="services">Laser Hair Removal<br>Velonix | Lip Filler</p>
  <p class="contact">(555) 287-1936 / www.WillowGlowLaser.com</p>
  <div class="social"><span></span><span></span></div>
</section>

</body>
</html>
```